Tarvon Letterhead

Looking for a design template for our company’s official letterheads & business cards.It has to be mainly white and include our company logo, website, social media handle, address, phone number. Visit our website to have an idea of our brand identity and colours. Please use the same font that we are using in our website.
Target Market(s)
Lubricants & Greases, Industrial markets, Automotive
Font styles to use
Other font styles liked:
- Saira Extra-Condensed
Colors
ffffff
000000
fbee3f
Requirements
Must have
- It must be consistent with our brand identity. It must use the same exact yellow (Pantone color: 102C) and black (Pantone color: K100) as our brand colors.
- Must also use our font attached (Saira.zip). It's called Saira Extra-Condensed.
- We intend to use the TARVON logo and not the small mini-TV logo.
- On the design we must include ALL of the following:
- E-mail: info@tarvonfluids.example
- @TarvonFluids
- www.tarvonfluids.example
- Address: P.O. Boc 4827, Qurain 73504, Kuwait
- Phone: (+965) 24718593
- Kuwait Morel Oils logo (attached). The logo attached is in Blue/Red but you can select one solid color for all of it such as BLACK or YELLOW depending on what background color you'll select.
Nice to have
- Like it to be as professional and as modern as possible. It has look clean, slick and classy.
Should not have
- Too many different colors.

```html
<!DOCTYPE html>
<html lang="en">
<head>
<meta charset="utf-8">
<title>Tarvon Business Card</title>
<link rel="stylesheet" href="https://fonts.googleapis.com/css2?family=Saira+Extra+Condensed:wght@600;800&family=Saira+Semi+Condensed:wght@400;500&display=swap">
<style>
  :root {
    --brand-yellow: #fbee3f;
    --brand-black: #1d1c1c;
    --ink: #222222;
    --card-white: #ffffff;
    --stage: #e4e4e4;
    --divider: #c9c9c9;
    --icon-grey: #b5b5b5;
  }
  * { box-sizing: border-box; margin: 0; padding: 0; }
  html, body { width: 1200px; height: 856px; overflow: hidden; }
  body {
    background: var(--stage);
    font-family: "Saira Semi Condensed", sans-serif;
    color: var(--ink);
    display: flex;
    flex-direction: column;
    align-items: center;
    justify-content: center;
    gap: 56px;
  }
  .card {
    position: relative;
    width: 560px;
    height: 320px;
    border-radius: 34px;
    overflow: hidden;
    box-shadow: 0 10px 24px rgba(0,0,0,0.12);
  }

  /* Front */
  .card--front { background: var(--card-white); }
  .front__brand {
    position: absolute;
    left: 24px; top: 104px;
    width: 232px;
    display: flex; align-items: center; justify-content: center; gap: 10px;
  }
  .brand-mark {
    width: 18px; height: 18px; flex: none;
    background: var(--brand-yellow);
  }
  .wordmark {
    font-family: "Saira Extra Condensed", sans-serif;
    font-weight: 800;
    line-height: 1;
    white-space: nowrap;
    color: var(--brand-black);
  }
  .card--front .wordmark { font-size: 46px; letter-spacing: 1px; }
  .front__divider {
    position: absolute;
    left: 268px; top: 40px;
    width: 1px; height: 190px;
    background: linear-gradient(to bottom, transparent, var(--divider) 20%, var(--divider) 80%, transparent);
  }
  .contact-list {
    position: absolute;
    left: 288px; top: 66px;
    width: 252px;
    list-style: none;
    display: flex; flex-direction: column; gap: 9px;
  }
  .contact-list li {
    display: flex; align-items: center; gap: 10px;
    font-size: 12px; line-height: 16px;
    white-space: nowrap;
  }
  .contact-icon { width: 14px; height: 14px; flex: none; }
  .contact-icon * { fill: none; stroke: var(--icon-grey); stroke-width: 1.4; }
  .parent-company {
    position: absolute;
    right: 34px; bottom: 50px;
    display: flex; align-items: center; gap: 8px;
  }
  .parent-company__dot {
    width: 20px; height: 20px; border-radius: 50%;
    background: var(--brand-black);
  }
  .parent-company__name {
    font-size: 10px; font-weight: 500;
    text-transform: uppercase; letter-spacing: 0.5px;
    white-space: nowrap;
    color: var(--brand-black);
  }
  .front__band { position: absolute; left: 0; bottom: 0; width: 560px; height: 40px; }

  /* Back */
  .card--back {
    background: var(--brand-black);
    display: flex; flex-direction: column;
    align-items: center; justify-content: center;
    gap: 18px;
  }
  .card--back .wordmark { color: var(--brand-yellow); font-size: 88px; letter-spacing: 2px; }
  .back__url {
    font-size: 16px; letter-spacing: 0.3px;
    color: var(--card-white);
  }
</style>
</head>
<body>

  <section class="card card--front" aria-label="Business card front">
    <div class="front__brand">
      <span class="brand-mark"></span>
      <span class="wordmark">TARVON</span>
    </div>

    <div class="front__divider"></div>

    <ul class="contact-list">
      <li>
        <svg class="contact-icon" viewBox="0 0 16 16"><path d="M8 14.5s-4.5-4.6-4.5-8a4.5 4.5 0 0 1 9 0c0 3.4-4.5 8-4.5 8z"/><circle cx="8" cy="6.5" r="1.6"/></svg>
        P.O. Boc 4827, Qurain 73504, Kuwait
      </li>
      <li>
        <svg class="contact-icon" viewBox="0 0 16 16"><path d="M4.5 2.5l2 2.5-1.2 1.5a8 8 0 0 0 4.2 4.2L11 9.5l2.5 2-1.5 2c-5 0-9.5-4.5-9.5-9.5z"/></svg>
        (+965) 24718593
      </li>
      <li>
        <svg class="contact-icon" viewBox="0 0 16 16"><rect x="2" y="4" width="12" height="8.5" rx="1"/><path d="M2.5 4.5L8 9l5.5-4.5"/></svg>
        info@tarvonfluids.example
      </li>
      <li>
        <svg class="contact-icon" viewBox="0 0 16 16"><circle cx="8" cy="8" r="6"/></svg>
        @TarvonFluids
      </li>
      <li>
        <svg class="contact-icon" viewBox="0 0 16 16"><circle cx="8" cy="8" r="6"/><ellipse cx="8" cy="8" rx="2.6" ry="6"/><path d="M2 8h12"/></svg>
        www.tarvonfluids.example
      </li>
    </ul>

    <div class="parent-company">
      <span class="parent-company__dot"></span>
      <span class="parent-company__name">Kuwait Morel Oils Co.</span>
    </div>

    <svg class="front__band" viewBox="0 0 560 40" preserveAspectRatio="none" aria-hidden="true">
      <polygon points="0,32 420,14 430,14 430,40 0,40" fill="var(--brand-yellow)"/>
      <polygon points="420,14 560,8 560,40 430,40" fill="var(--brand-black)"/>
    </svg>
  </section>

  <section class="card card--back" aria-label="Business card back">
    <span class="wordmark">TARVON</span>
    <span class="back__url">www.tarvonfluids.example</span>
  </section>

</body>
</html>
```